KALMORA Banner

I need a banner for a outpatient (poli clinic) psychiatric clinic/ mental health care center.
The name of the out-patient clinic is ' KALMORA ' . It is written in capitals. The colour we use is green. Just look at the uploaded files and on our website: WWW.KALMORA.NL

KALMORA is mainly based in the city Groningen, the Netherlands (Holland).

If it is possible, I would also like to have a QR-code of our website on the banner. It should be a vertical banner.

We want to print big vertical flags/ roll-up banners

Reason: I just extended the deadline. I will attach more examples of what I want.

To all designers,

Sorry for not giving feedback on your designs. I have attached a picture that I want to be used as background.

So the colour of the banner should be greenish, with the text: "  KALMORA " 
Further more I would like to have the website on the banner: " WWW.KALMORA.NL "
The logo of KALMORA must also be on the banner
And also a small QR-code

I will extend the deadline till february 13th

thanks,

Bram

Reason: Dear designers, Sorry for not reacting. I was ill and could not work. best regards, Bram

Industry/Entity Type

Mental Health

Requirements
Must have
• The logo of KALMORA must be in the design. For the right colour just take a look at the attached files and our website: www.KALMORA.NL

```html
<!DOCTYPE html>
<html lang="nl">
<head>
<meta charset="utf-8">
<title>KALMORA Banner</title>
<link rel="stylesheet" href="https://fonts.googleapis.com/css2?family=Source+Sans+3:wght@400&display=swap">
<style>
  :root {
    --brand-green: #0c7f42;
    --mark-green-light: #dcefe3;
    --mark-green-mid: #b9dcc6;
    --paper: #ffffff;
    --name-grey: #6e6e6e;
    --bullet-grey: #8c8c8c;
    --text-green: #13864a;
  }
  html, body {
    margin: 0;
    padding: 0;
    overflow: hidden;
    background: var(--paper);
  }
  .banner {
    position: relative;
    width: 1200px;
    height: 2892px;
    background: var(--paper);
    overflow: hidden;
    font-family: "Source Sans 3", "Myriad Pro", sans-serif;
  }
  .band {
    position: absolute;
    left: 0;
    width: 100%;
    background: var(--brand-green);
  }
  .band--top {
    top: 0;
    height: 422px;
  }
  .band--bottom {
    bottom: 0;
    height: 347px;
    display: flex;
    align-items: center;
    justify-content: center;
  }
  .brand-mark {
    position: absolute;
    top: 740px;
    left: 320px;
    width: 560px;
    height: 560px;
    background: linear-gradient(160deg, var(--mark-green-light), var(--mark-green-mid));
  }
  .brand-name {
    position: absolute;
    top: 1410px;
    left: 0;
    width: 100%;
    margin: 0;
    text-align: center;
    font-weight: 400;
    font-size: 204px;
    line-height: 1;
    letter-spacing: 20px;
    text-indent: 20px;
    color: var(--name-grey);
  }
  .topics {
    position: absolute;
    top: 1710px;
    left: 440px;
    margin: 0;
    padding: 0;
    list-style: none;
  }
  .topics li {
    position: relative;
    padding-left: 70px;
    font-size: 76px;
    line-height: 108px;
    color: var(--text-green);
  }
  .topics li::before {
    content: "";
    position: absolute;
    left: 6px;
    top: 50%;
    width: 17px;
    height: 17px;
    margin-top: -4px;
    border-radius: 50%;
    background: var(--bullet-grey);
  }
  .web-address {
    margin: 0;
    font-size: 102px;
    font-weight: 400;
    color: var(--paper);
    letter-spacing: 1px;
  }
</style>
</head>
<body>
  <main class="banner">
    <div class="band band--top"></div>

    <div class="brand-mark" role="img" aria-label="KALMORA logo symbol"></div>

    <h1 class="brand-name">KALMORA</h1>

    <ul class="topics">
      <li>Missie/visie</li>
      <li>Rechten/plichten</li>
      <li>Klachten</li>
      <li>Toezicht</li>
      <li>Vergoeding</li>
      <li>Vacatures</li>
    </ul>

    <footer class="band band--bottom">
      <p class="web-address">www.kalmora.nl</p>
    </footer>
  </main>
</body>
</html>
```